New Web Design Project

Require a website for The Bramwell Harvest. All relevant information is in the uploaded files.

website to be responsive to work on mobile.

Required in html5, css

Coding

Coded - Design and coding required

Number of Pages Required

3 page

```html
<!DOCTYPE html>
<html lang="en">
<head>
<meta charset="utf-8">
<title>The Bramwell Harvest Company</title>
<link href="https://fonts.googleapis.com/css2?family=Montserrat:wght@400;500;600;700&family=Open+Sans:wght@400;600&display=swap" rel="stylesheet">
<style>
:root{
  --green:#8dc63f;
  --orange:#f7941d;
  --ink:#222;
  --text:#444;
  --muted:#777;
  --grey-band:#ebebeb;
  --news-band:#f2f2f2;
  --white:#fff;
  --line:#bdbdbd;
}
*{margin:0;padding:0;box-sizing:border-box}
html,body{width:1200px;height:4422px;overflow:hidden;background:var(--white)}
body{font-family:"Open Sans",sans-serif;color:var(--text);position:relative}
section,header,footer{position:absolute;left:0;width:1200px}
.h-sec{font-family:"Montserrat",sans-serif;font-size:33px;font-weight:400;color:var(--ink);text-align:center;position:absolute;left:0;width:1200px;letter-spacing:.5px}
.h-sec b{font-weight:700}
.h-sec::after{content:"";display:block;width:50px;height:3px;background:var(--orange);margin:12px auto 0}
.connector{position:absolute;left:599px;width:1px;background:#888}
.connector::after{content:"";position:absolute;left:-3px;bottom:-4px;width:7px;height:7px;border-radius:50%;background:#888}

/* header */
.site-header{top:0;height:91px;background:var(--white)}
.brand{position:absolute;left:88px;top:24px;display:flex;align-items:center;gap:10px}
.brand-dot{width:42px;height:42px;border-radius:50%;background:var(--orange)}
.brand-name{font-family:"Montserrat",sans-serif;font-weight:700;font-size:22px;color:#333;line-height:1.05}
.main-nav{position:absolute;top:38px;left:400px;font-family:"Montserrat",sans-serif;font-size:14px;color:#444}
.nav-item{position:absolute;white-space:nowrap}
.nav-item.active{color:var(--orange);font-weight:600}
.nav-sep{position:absolute;color:#aaa}

/* hero */
.hero{top:91px;height:680px;overflow:hidden}
.hero-photo{position:absolute;inset:0;background:linear-gradient(180deg,#1c2a4a 0%,#2d3d63 35%,#6b4a3a 58%,#c9783a 66%,#2a2c3a 72%,#1a2236 100%)}
.hero-mark{position:absolute;left:565px;top:170px;width:70px;height:70px;border-radius:50%;background:var(--white)}
.hero-welcome{position:absolute;top:262px;width:1200px;text-align:center;font-family:"Montserrat",sans-serif;font-size:35px;letter-spacing:8px;color:var(--white)}
.hero-title{position:absolute;top:310px;width:1200px;text-align:center;font-family:"Montserrat",sans-serif;font-weight:700;font-size:47px;color:var(--white)}
.btn-hero{position:absolute;left:508px;top:387px;width:180px;height:46px;border-radius:23px;background:var(--green);color:var(--white);font-family:"Montserrat",sans-serif;font-weight:600;font-size:15px;display:flex;align-items:center;justify-content:center;gap:6px}
.hero-arrow{position:absolute;top:295px}
.hero-wave{position:absolute;left:0;top:560px}

/* about */
.about{top:771px;height:960px}
.eyebrow{position:absolute;top:100px;width:1200px;text-align:center;font-family:"Montserrat",sans-serif;font-size:20px;color:#444}
.about-title{position:absolute;top:126px;width:1200px;text-align:center;font-family:"Montserrat",sans-serif;font-weight:700;font-size:38px;color:var(--ink)}
.about-title span{border-bottom:3px solid var(--orange);padding-bottom:2px}
.about-copy{position:absolute;left:160px;top:205px;width:880px;text-align:center;font-size:15px;line-height:30px;color:#444}
.feature{position:absolute;width:300px;font-size:14px;line-height:21px;color:#444}
.feature h3{font-family:"Montserrat",sans-serif;font-size:15px;font-weight:700;color:#333;margin-bottom:2px}
.feature.right-al{text-align:right}
.feature.center{text-align:center}
.diagram{position:absolute;left:0;top:0}
.about-photo{position:absolute;left:460px;top:425px;width:280px;height:316px;border-radius:50%;background:linear-gradient(120deg,#7cbf3a 0%,#b6d77a 50%,#f08a1c 100%)}

/* services */
.services{top:1734px;height:550px;background:var(--grey-band)}
.svc{position:absolute;top:136px;width:338px;height:338px;border-radius:50%;text-align:center;font-family:"Montserrat",sans-serif}
.svc.green{left:70px;background:var(--green);color:var(--white)}
.svc.white{left:429px;background:var(--white);color:#333;box-shadow:0 8px 26px rgba(0,0,0,.18);border:10px solid #f4f4f4}
.svc.orange{left:785px;background:var(--orange);color:var(--white)}
.svc-icon{width:106px;height:106px;border-radius:50%;margin:45px auto 0;display:flex;align-items:center;justify-content:center}
.svc.white .svc-icon{margin-top:35px}
.green .svc-icon{background:var(--white)}
.green .svc-icon i{background:var(--green)}
.white .svc-icon{background:var(--orange)}
.white .svc-icon i{background:var(--white)}
.orange .svc-icon{background:var(--green)}
.orange .svc-icon i{background:var(--white)}
.svc-icon i{display:block;width:40px;height:40px;border-radius:50%}
.svc h3{font-size:21px;font-weight:600;margin-top:22px}
.svc p{font-family:"Open Sans",sans-serif;font-size:12px;line-height:19px;width:250px;margin:10px auto 0}
.svc-caret{margin-top:16px}

/* people */
.people{top:2284px;height:498px}
.person-photo{position:absolute;top:176px;width:186px;height:204px;border:1px solid var(--orange);padding:6px;background:var(--white)}
.person-photo div{width:100%;height:100%;background:linear-gradient(180deg,#e9e9e9 0%,#d8d8d8 55%,#2f3440 56%,#22262e 100%)}
.person{position:absolute;top:185px;width:270px;font-size:11px;line-height:18px;color:#555}
.person h3{font-family:"Montserrat",sans-serif;font-size:17px;font-weight:700;color:#222}
.person .role{font-family:"Montserrat",sans-serif;font-size:17px;color:#444;margin-bottom:10px}
.btn-bio{display:inline-block;margin-top:20px;width:134px;height:33px;border:2px solid var(--green);color:var(--green);font-family:"Montserrat",sans-serif;font-weight:600;font-size:10px;text-align:center;line-height:29px}

/* news */
.news{top:2782px;height:609px;background:var(--news-band)}
.news-card{position:absolute;top:144px;width:316px;height:385px;background:var(--white);border:1px solid #ddd}
.news-img{height:199px}
.news-body{padding:18px 30px 0}
.news-date{font-family:"Montserrat",sans-serif;font-size:13px;color:var(--orange);font-weight:500}
.news-body h3{font-family:"Montserrat",sans-serif;font-size:16px;font-weight:700;color:#333;line-height:20px;margin-top:8px}
.news-body p{font-size:12px;line-height:19px;color:#777;margin-top:8px}
.news-more{display:block;margin-top:14px;font-family:"Montserrat",sans-serif;font-weight:700;font-size:12px;color:var(--green)}

/* message */
.message{top:3391px;height:549px;overflow:hidden}
.message-photo{position:absolute;inset:0;background:linear-gradient(180deg,#1d1d1d 0%,#3a3a3a 45%,#555 62%,#2b2b2b 78%,#1a1a1a 100%)}
.message .h-sec{top:70px;color:var(--white)}
.field{position:absolute;background:var(--white);border:1px solid #ccc;font-size:15px;color:#555;padding:0 20px;display:flex;align-items:center}
.field.area{align-items:flex-start;padding-top:18px}
.btn-send{position:absolute;left:470px;top:392px;width:244px;height:55px;border-radius:28px;background:var(--orange);color:var(--white);font-family:"Montserrat",sans-serif;font-weight:600;font-size:18px;display:flex;align-items:center;justify-content:center}

/* footer */
.site-footer{top:3940px;height:482px}
.f-col{position:absolute;top:98px;font-size:13px;color:#444}
.f-col h4{font-family:"Montserrat",sans-serif;font-weight:700;font-size:18px;color:#222}
.f-col h4::after{content:"";display:block;width:30px;height:3px;background:var(--orange);margin:10px 0 18px}
.f-col ul{list-style:none}
.f-col li{line-height:31px}
.contact-row{display:flex;gap:12px;align-items:flex-start;margin-bottom:14px;line-height:19px}
.socials{display:flex;gap:8px;margin-top:6px}
.socials span{width:34px;height:34px;border-radius:50%;border:2px solid var(--orange)}
.newsletter-field{width:268px;height:40px;border:1px solid #bbb;font-size:12px;padding:0 14px;display:flex;align-items:center;color:#555}
.btn-sub{margin-top:14px;width:138px;height:38px;border-radius:19px;background:var(--green);color:var(--white);font-family:"Montserrat",sans-serif;font-weight:600;font-size:13px;display:flex;align-items:center;justify-content:center}
.footer-rule{position:absolute;top:378px;left:93px;width:1014px;height:1px;background:#ddd}
.footer-mark{position:absolute;left:572px;top:350px;width:56px;height:56px;border-radius:50%;background:var(--orange);border:6px solid var(--white)}
.copyright{position:absolute;top:420px;width:1200px;text-align:center;font-size:13px;color:#666}
</style>
</head>
<body>

<header class="site-header">
  <div class="brand"><div class="brand-dot"></div><div class="brand-name">The Bramwell<br>Harvest</div></div>
  <nav class="main-nav">
    <span class="nav-item active" style="left:12px">HOME</span>
    <span class="nav-sep" style="left:79px">|</span>
    <span class="nav-item" style="left:116px">ABOUT US</span>
    <span class="nav-sep" style="left:215px">|</span>
    <span class="nav-item" style="left:255px">SERVICES</span>
    <span class="nav-sep" style="left:352px">|</span>
    <span class="nav-item" style="left:390px">PEOPLE</span>
    <span class="nav-sep" style="left:458px">|</span>
    <span class="nav-item" style="left:512px">NEWS</span>
    <span class="nav-sep" style="left:584px">|</span>
    <span class="nav-item" style="left:619px">CONTACT US</span>
  </nav>
</header>

<section class="hero">
  <div class="hero-photo" role="img" aria-label="City skyline at night with a tall tower reflected on the lake"></div>
  <div class="hero-mark"></div>
  <div class="hero-welcome">WELCOME TO</div>
  <h1 class="hero-title">THE BRAMWELL HARVEST COMPANY</h1>
  <div class="btn-hero">LEARN MORE <span>›</span></div>
  <svg class="hero-arrow" style="left:26px" width="26" height="44" viewBox="0 0 26 44"><path d="M22 4 L5 22 L22 40" fill="none" stroke="#fff" stroke-width="3"/></svg>
  <svg class="hero-arrow" style="right:26px" width="26" height="44" viewBox="0 0 26 44"><path d="M4 4 L21 22 L4 40" fill="none" stroke="#fff" stroke-width="3"/></svg>
  <svg class="hero-wave" width="1200" height="120" viewBox="0 0 1200 120">
    <path d="M0 88 C200 60 360 40 560 60 C760 80 900 62 1200 0 L1200 120 L0 120 Z" fill="var(--orange)"/>
    <path d="M0 108 C220 70 380 60 580 78 C780 96 930 70 1200 20 L1200 120 L0 120 Z" fill="#fff"/>
  </svg>
</section>

<div class="connector" style="top:730px;height:92px"></div>

<section class="about">
  <div class="eyebrow">WHO WE ARE</div>
  <h2 class="about-title">THE BRAMWELL <span>HARVEST</span></h2>
  <p class="about-copy">The Bramwell Harvest Company was incorporated with the objective of introducing new vendors to the Canadian market through a trusted and mutual business relation It was set up by Dario Kessler and Theo Marlowe who have a combined experience of over 45 years in the fresh produce business. With Dario's expertise in global sourcing and Theo's vast connection and know how of the Canadian market, we have helped our existing partners</p>

  <svg class="diagram" width="1200" height="960" viewBox="0 0 1200 960">
    <path d="M470 486 A176 176 0 1 0 730 486" fill="none" stroke="#ccc" stroke-width="2"/>
    <circle cx="470" cy="486" r="6" fill="var(--green)"/>
    <circle cx="730" cy="486" r="6" fill="var(--green)"/>
    <circle cx="439" cy="672" r="6" fill="var(--green)"/>
    <circle cx="763" cy="664" r="6" fill="var(--green)"/>
    <circle cx="600" cy="780" r="6" fill="var(--green)"/>
  </svg>
  <div class="about-photo" role="img" aria-label="Round collage of warehouse staff and fresh produce"></div>

  <div class="feature right-al" style="left:102px;top:465px"><h3>SUB HEADING</h3>Lorem ipsum dolor sit amet,<br>consectetur adipiscing elit, sed do</div>
  <div class="feature" style="left:790px;top:465px"><h3>SUB HEADING</h3>Lorem ipsum dolor sit amet,<br>consectetur adipiscing elit, sed do</div>
  <div class="feature right-al" style="left:89px;top:648px"><h3>SUB HEADING</h3>Lorem ipsum dolor sit amet,<br>consectetur adipiscing elit, sed do eiusmod</div>
  <div class="feature" style="left:798px;top:648px"><h3>SUB HEADING</h3>Lorem ipsum dolor sit amet,<br>consectetur adipiscing elit, sed do eiusmod</div>
  <div class="feature center" style="left:450px;top:812px"><h3>SUB HEADING</h3>Lorem ipsum dolor sit amet, consectetur<br>adipiscing elit, sed do</div>
</section>

<div class="connector" style="top:1708px;height:58px;z-index:2"></div>

<section class="services">
  <h2 class="h-sec" style="top:52px">OUR <b>SERVICES</b></h2>
  <div class="svc green">
    <div class="svc-icon"><i></i></div>
    <h3>GLOBAL SERVICE</h3>
    <p>Lorem ipsum dolor sit amet, consectetur adipiscing elit, sed do eiusmo</p>
    <svg class="svc-caret" width="32" height="18" viewBox="0 0 32 18"><path d="M3 3 L16 15 L29 3" fill="none" stroke="#fff" stroke-width="3"/></svg>
  </div>
  <div class="svc white">
    <div class="svc-icon"><i></i></div>
    <h3>PRODUCE TRADING</h3>
    <p>Lorem ipsum dolor sit amet, consectetur adipiscing elit, sed do eiusmod</p>
    <svg class="svc-caret" width="32" height="18" viewBox="0 0 32 18"><path d="M3 3 L16 15 L29 3" fill="none" stroke="var(--orange)" stroke-width="3"/></svg>
  </div>
  <div class="svc orange">
    <div class="svc-icon"><i></i></div>
    <h3>CONSULTING SERVICE</h3>
    <p>Lorem ipsum dolor sit amet, consectetur adipiscing elit, sed do eiusmod e</p>
    <svg class="svc-caret" width="32" height="18" viewBox="0 0 32 18"><path d="M3 3 L16 15 L29 3" fill="none" stroke="#fff" stroke-width="3"/></svg>
  </div>
</section>

<div class="connector" style="top:2262px;height:66px;z-index:2;background:#333"></div>

<section class="people">
  <h2 class="h-sec" style="top:70px">OUR <b>PEOPLE</b></h2>
  <div class="person-photo" style="left:98px"><div role="img" aria-label="Portrait of the founder in a dark suit"></div></div>
  <div class="person" style="left:311px">
    <h3>Theo Marlowe</h3>
    <div class="role">Founder</div>
    Theo is a detail oriented manager &amp; a leader who closely watches the P&amp;L but never loses sight of the strategic perspective. I have worked with Theo for about 5 years &amp; I always found him to be a great leader with a strong motivational
    <br><span class="btn-bio">READ FULL BIO</span>
  </div>
  <div class="person-photo" style="left:649px"><div role="img" aria-label="Portrait of the founder and president in a dark suit"></div></div>
  <div class="person" style="left:870px">
    <h3>Dario Kessler</h3>
    <div class="role">Founder &amp; President</div>
    Dario is a detail oriented manager &amp; a leader who closely watches the P&amp;L but never loses sight of the strategic perspective. I have worked with Dario for about 5 years &amp; I always found him to be a great leader with a strong motivational
    <br><span class="btn-bio">READ FULL BIO</span>
  </div>
</section>

<div class="connector" style="top:2752px;height:60px;z-index:2"></div>

<section class="news">
  <h2 class="h-sec" style="top:58px">NEWS <b>&amp; INSIGHTS</b></h2>
  <article class="news-card" style="left:98px">
    <div class="news-img" role="img" aria-label="Business people reviewing documents at a laptop" style="background:linear-gradient(135deg,#2d3b4a,#9aa6b2 60%,#e6e9ec)"></div>
    <div class="news-body"><div class="news-date">20 AUG 2020</div><h3>Lorem ipsum dolor sit amet, consectetur adipiscinelit,</h3><p>Excepteur sint occaecat cupidatat non proident, sunt in culpa qui</p><span class="news-more">LEARN MORE</span></div>
  </article>
  <article class="news-card" style="left:443px">
    <div class="news-img" role="img" aria-label="Forklift lifting sacks in a warehouse" style="background:linear-gradient(135deg,#5a3a20,#d98a2c 50%,#efe2c8)"></div>
    <div class="news-body"><div class="news-date">20 AUG 2020</div><h3>Lorem ipsum dolor sit amet, consectetur adipiscinelit,</h3><p>Excepteur sint occaecat cupidatat non proident, sunt in culpa qui</p><span class="news-more">LEARN MORE</span></div>
  </article>
  <article class="news-card" style="left:788px">
    <div class="news-img" role="img" aria-label="Bottling line filled with orange juice bottles" style="background:linear-gradient(180deg,#1f3f8a,#4a78c8 55%,#f5b11c 70%,#2a4f9c)"></div>
    <div class="news-body"><div class="news-date">20 AUG 2020</div><h3>Lorem ipsum dolor sit amet, consectetur adipiscinelit,</h3><p>Excepteur sint occaecat cupidatat non proident, sunt in culpa qui</p><span class="news-more">LEARN MORE</span></div>
  </article>
</section>

<div class="connector" style="top:3332px;height:102px;z-index:2;background:var(--green)"></div>

<section class="message">
  <div class="message-photo" role="img" aria-label="Black and white city skyline over water"></div>
  <h2 class="h-sec" style="color:#fff"><b>LEAVE US A</b> MESSAGE</h2>
  <div class="field" style="left:134px;top:172px;width:458px;height:54px">Your Name *</div>
  <div class="field" style="left:134px;top:240px;width:458px;height:54px">Phone Number*</div>
  <div class="field" style="left:134px;top:309px;width:458px;height:54px">E-mail address*</div>
  <div class="field area" style="left:606px;top:172px;width:459px;height:191px">Write Message</div>
  <div class="btn-send">SEND MESSAGE</div>
</section>

<footer class="site-footer">
  <div class="f-col" style="left:117px;width:260px">
    <h4>Contact Us</h4>
    <div class="contact-row">
      <svg width="18" height="20" viewBox="0 0 18 20"><path d="M9 1 C4.5 1 2 4 2 7.5 C2 12 9 19 9 19 C9 19 16 12 16 7.5 C16 4 13.5 1 9 1 Z" fill="var(--green)"/><circle cx="9" cy="7.5" r="2.6" fill="#fff"/></svg>
      <span>123 Avenue name, City name<br>25252, United States</span>
    </div>
    <div class="contact-row">
      <svg width="18" height="16" viewBox="0 0 18 16"><path d="M4 2 L7 5 L5.5 7 C6.5 9 8 10.5 10 11.5 L12 10 L15 13 L13 15 C7 14 3 10 2 4 Z" fill="var(--green)"/></svg>
      <span>123-456-7890</span>
    </div>
    <div class="contact-row">
      <svg width="18" height="14" viewBox="0 0 18 14"><rect x="1" y="1" width="16" height="12" fill="var(--green)"/><path d="M1 1 L9 8 L17 1" fill="none" stroke="#fff" stroke-width="1.5"/></svg>
      <span>info@bramwellharvest.com</span>
    </div>
    <div class="socials"><span></span><span></span><span></span><span></span></div>
  </div>
  <div class="f-col" style="left:424px">
    <h4>Information</h4>
    <ul><li>About Us</li><li>Why Choose Us</li><li>Our People</li><li>Clients</li><li>Contact Us</li></ul>
  </div>
  <div class="f-col" style="left:647px">
    <h4>Resources</h4>
    <ul><li>Services</li><li>Support</li><li>Term of Use</li><li>News</li><li>Privacy Policy</li></ul>
  </div>
  <div class="f-col" style="left:855px">
    <h4>Sign Up Newsletter</h4>
    <div class="newsletter-field">Your Email address</div>
    <div class="btn-sub">SUBSCRIBE</div>
  </div>
  <div class="footer-rule"></div>
  <div class="footer-mark"></div>
  <div class="copyright">Copyright ©&nbsp; 2010-2020 The Bramwell Harvest All rights reserved.</div>
</footer>

</body>
</html>
```